Stationery Design Project

We need letterhead and business cards designed for our consulting firm. Color scheme, mostly deep blue (see logo). We are a commercial consulting work out firm, nationwide (large loans, $10MM and up). Visit our website for more info.
Updates

Project Deadline Extended
Reason: Meeting tomorrow morning to make final final decision. Would like this project to stay open to be able to provide feed back and receive final edits and approve. Thank you!!!

Target Market(s)

High end investors

Industry/Entity Type

Business

Requirements
Must have
• Letterhead must have the logo and the address

4817 Larkmoor Avenue, Suite 210, San Diego, CA 92107
Nice to have
• It would be nice to incorporate a watermark of all or some portion of the logo on the letterhead, or at least for the 2nd sheets.

Maybe our phone number: 858.555.0174
and/or webiste: www.tollandridgecap.example
Should not have
• Target users and audience of this will be men so, frilly or whimsical type designs are not preferred.

```html
<!DOCTYPE html>
<html lang="en">
<head>
<meta charset="utf-8">
<title>Tolland Ridge Capital — Stationery</title>
<link rel="stylesheet" href="https://fonts.googleapis.com/css2?family=Cinzel:wght@400;600&family=Arimo:wght@400;700&display=swap">
<style>
  :root {
    --page: #ffffff;
    --ink-grey: #7b7b7b;
    --ink-dark: #333333;
    --mark-faint: #f1f3f5;
    --brand-blue: #0b7fc4;
    --card-edge: #d9dadb;
    --card-bar: #1f5f86;
    --shadow: rgba(0, 0, 0, 0.45);
  }
  * { box-sizing: border-box; margin: 0; padding: 0; }
  html, body {
    width: 763px;
    height: 1200px;
    overflow: hidden;
    background: var(--page);
  }
  .canvas {
    position: relative;
    width: 763px;
    height: 1200px;
  }

  /* Letterhead */
  .letterhead {
    position: absolute;
    left: 83px;
    top: 29px;
    width: 552px;
    height: 780px;
    background: var(--page);
    border: 1px solid #9a9a9a;
    box-shadow: 3px 4px 6px var(--shadow);
  }
  .letterhead__name {
    position: absolute;
    top: 12px;
    left: 0;
    width: 100%;
    text-align: center;
    font-family: "Cinzel", serif;
    font-weight: 400;
    font-size: 56px;
    letter-spacing: 1px;
    color: var(--ink-grey);
    line-height: 1;
  }
  .letterhead__address {
    position: absolute;
    top: 72px;
    left: 0;
    width: 100%;
    text-align: center;
    font-family: "Arimo", sans-serif;
    font-size: 10.5px;
    text-transform: uppercase;
    color: var(--ink-dark);
  }
  .letterhead__watermark {
    position: absolute;
    top: 380px;
    left: 0;
    width: 100%;
    text-align: center;
    font-family: "Cinzel", serif;
    font-weight: 400;
    font-size: 58px;
    color: var(--mark-faint);
    line-height: 1;
  }
  .letterhead__watermark-square {
    position: absolute;
    top: 270px;
    left: 236px;
    width: 80px;
    height: 80px;
    background: var(--mark-faint);
  }
  .letterhead__sign {
    position: absolute;
    top: 668px;
    left: 0;
    width: 100%;
    display: flex;
    flex-direction: column;
    align-items: center;
    gap: 10px;
  }
  .brand-square {
    width: 34px;
    height: 34px;
    background: var(--brand-blue);
  }
  .brand-name {
    font-family: "Cinzel", serif;
    font-weight: 400;
    font-size: 22px;
    color: var(--ink-grey);
    line-height: 1;
  }
  .letterhead__band {
    position: absolute;
    left: 0;
    bottom: 0;
    width: 100%;
    height: 29px;
    background: var(--brand-blue);
    display: flex;
    align-items: center;
    justify-content: center;
    font-family: "Arimo", sans-serif;
    font-weight: 700;
    font-size: 12.5px;
    color: #ffffff;
  }

  /* Business card */
  .card {
    position: absolute;
    left: 172px;
    top: 873px;
    width: 376px;
    height: 234px;
    background: radial-gradient(ellipse at center, #ffffff 55%, var(--card-edge) 100%);
    border: 1px solid #8a8a8a;
    box-shadow: 3px 4px 6px var(--shadow);
  }
  .card__bar {
    position: absolute;
    top: 50px;
    width: 5px;
    height: 134px;
    background: var(--card-bar);
  }
  .card__bar--left { left: 3px; }
  .card__bar--right { right: 3px; }
  .card__sign {
    position: absolute;
    top: 66px;
    left: 0;
    width: 100%;
    display: flex;
    flex-direction: column;
    align-items: center;
    gap: 9px;
  }
  .card__sign .brand-square { width: 30px; height: 30px; }
  .card__sign .brand-name { font-size: 19px; }
  .card__web {
    font-family: "Arimo", sans-serif;
    font-size: 10.5px;
    color: var(--brand-blue);
  }
  .card__contact {
    position: absolute;
    bottom: 9px;
    left: 0;
    width: 100%;
    text-align: center;
    font-family: "Arimo", sans-serif;
    font-size: 7.5px;
    color: var(--ink-dark);
  }
</style>
</head>
<body>
<main class="canvas">

  <section class="letterhead" aria-label="Letterhead">
    <h1 class="letterhead__name">TOLLAND RIDGE</h1>
    <p class="letterhead__address">4817 Larkmoor Avenue, Suite 210, San Diego, CA 92107</p>

    <div class="letterhead__watermark-square" aria-hidden="true"></div>
    <div class="letterhead__watermark" aria-hidden="true">Tolland Ridge</div>

    <div class="letterhead__sign">
      <span class="brand-square" aria-hidden="true"></span>
      <span class="brand-name">Tolland Ridge Capital</span>
    </div>

    <footer class="letterhead__band">www.tollandridgecap.example</footer>
  </section>

  <section class="card" aria-label="Business card">
    <span class="card__bar card__bar--left" aria-hidden="true"></span>
    <span class="card__bar card__bar--right" aria-hidden="true"></span>

    <div class="card__sign">
      <span class="brand-square" aria-hidden="true"></span>
      <span class="brand-name">Tolland Ridge Capital</span>
      <span class="card__web">www.tollandridgecap.example</span>
    </div>

    <p class="card__contact">4817 Larkmoor Avenue, Suite 210, San Diego, CA 92107 &nbsp;|&nbsp; 858.555.0174</p>
  </section>

</main>
</body>
</html>
```